Product Photos Need Photoshop Designing

We have taken product photos and photo shopped them ourselves, however they are not at a professional standard. We would like to see what some professionals can do with our images.
We really like the black backgrounds with reflective ground. We have provided the images we have photo shopped for your reference to give you an idea of what the images need to say in terms of text. We like the blue colour from our logo to be used in the image text.
We have also attached the original images for you to play around with and see what you can come up with.
All in all we are looking for sharp, professional product photos for our website. Small file types would be appreciated to allow the website to load fast. Thank you.
PS: We will have a LOT of ongoing work for the right designer.
Target Market(s)
Automotive Industry
Colors
Designer to choose colors to be used in the design.

```html
<!DOCTYPE html>
<html lang="en">
<head>
<meta charset="utf-8">
<title>LED Headlight Kit – Feature Panels</title>
<link rel="stylesheet" href="https://fonts.googleapis.com/css2?family=Barlow+Condensed:ital,wght@1,600;1,700;1,800&display=swap">
<style>
  :root {
    --accent-blue: #1d9be0;
    --text-light: #dcdcdc;
    --bg-top: #3b3b3b;
    --bg-mid: #2a2a2a;
    --bg-floor: #1a1a1a;
    --divider: #b9b9b9;
    --photo-metal: #8a8d90;
    --photo-metal-dark: #4a4c4e;
    --photo-rubber: #262626;
    --photo-rubber-dark: #121212;
  }
  * { margin: 0; padding: 0; box-sizing: border-box; }
  html, body { width: 1200px; height: 3400px; overflow: hidden; background: #111; }
  .canvas { position: relative; width: 1200px; height: 3400px; }
  .feature-panel {
    position: absolute; left: 0; width: 1200px; height: 850px; overflow: hidden;
    background:
      radial-gradient(ellipse 70% 55% at 50% 40%, rgba(255,255,255,0.10), rgba(255,255,255,0) 70%),
      linear-gradient(180deg, var(--bg-top) 0%, var(--bg-mid) 62%, var(--bg-floor) 100%);
    border-bottom: 5px solid var(--divider);
  }
  .feature-panel:last-child { border-bottom: none; }
  .feature-panel::after {
    content: ""; position: absolute; left: 0; right: 0; top: 66%; height: 3px;
    background: linear-gradient(90deg, rgba(255,255,255,0), rgba(255,255,255,0.12), rgba(255,255,255,0));
  }
  .panel-colour { top: 0; }
  .panel-install { top: 850px; }
  .panel-cooling { top: 1700px; }
  .panel-driver { top: 2550px; }

  .product-photo { position: absolute; z-index: 1; border-radius: 24px; }
  .photo-metal {
    background: radial-gradient(ellipse 60% 60% at 50% 40%, var(--photo-metal), var(--photo-metal-dark) 100%);
  }
  .photo-rubber {
    background: radial-gradient(ellipse 70% 70% at 50% 40%, var(--photo-rubber), var(--photo-rubber-dark) 100%);
  }
  .photo-bulb-bands { left: 120px; top: 20px; width: 360px; height: 780px; }
  .photo-connectors { left: 0; top: 500px; width: 1200px; height: 200px; border-radius: 0; }
  .photo-bulb-spread { left: 80px; top: 120px; width: 440px; height: 660px; }
  .photo-driver { left: 160px; top: 50px; width: 400px; height: 800px; border-radius: 24px 24px 0 0; }

  .feature-copy {
    position: absolute; z-index: 2;
    font-family: "Barlow Condensed", "Arial Narrow", sans-serif;
    font-style: italic; text-transform: uppercase; line-height: 0.95;
    letter-spacing: 0.5px;
  }
  .feature-copy .headline { display: block; color: var(--accent-blue); font-weight: 800; }
  .feature-copy .subline { display: block; color: var(--text-light); font-weight: 700; }

  .copy-colour { left: 652px; top: 318px; }
  .copy-colour .headline { font-size: 176px; }
  .copy-colour .subline { font-size: 96px; margin-top: -4px; }

  .copy-install { left: 0; right: 0; top: 180px; text-align: center; }
  .copy-install .headline { font-size: 98px; }
  .copy-install .subline { font-size: 84px; }

  .copy-cooling { left: 620px; top: 356px; }
  .copy-cooling .headline { font-size: 60px; }
  .copy-cooling .subline { font-size: 86px; margin-top: 4px; }

  .copy-driver { left: 620px; top: 438px; }
  .copy-driver .headline { font-size: 78px; }
  .copy-driver .subline { font-size: 60px; }
</style>
</head>
<body>
<main class="canvas">
  <section class="feature-panel panel-colour">
    <div class="product-photo photo-metal photo-bulb-bands" role="img" aria-label="Product photo: lit LED headlight bulb standing on four copper heat bands"></div>
    <h2 class="feature-copy copy-colour"><span class="headline">6000K</span><span class="subline">Pure White</span></h2>
  </section>

  <section class="feature-panel panel-install">
    <h2 class="feature-copy copy-install"><span class="headline">Plug &amp; Play</span><span class="subline">Easy Installation</span></h2>
    <div class="product-photo photo-rubber photo-connectors" role="img" aria-label="Product photo: two black waterproof wiring connectors about to be joined"></div>
  </section>

  <section class="feature-panel panel-cooling">
    <div class="product-photo photo-metal photo-bulb-spread" role="img" aria-label="Product photo: LED headlight bulb with four braided copper cooling bands fanned out"></div>
    <h2 class="feature-copy copy-cooling"><span class="headline">Heat Management</span><span class="subline">4 Copper Bands</span></h2>
  </section>

  <section class="feature-panel panel-driver">
    <div class="product-photo photo-rubber photo-driver" role="img" aria-label="Product photo: black finned aluminium driver module with cable"></div>
    <h2 class="feature-copy copy-driver"><span class="headline">Smart Driver</span><span class="subline">Superior Performance</span></h2>
  </section>
</main>
</body>
</html>
```